Infographics about Plumline Census

Hello, we are NexoraFlux, a leading Big Data and Data Science consultancy firm from The Netherlands. We are looking for an awesome infographic.

Introduction
In order to create a better understanding of the status of Big Data in our little country, together with the biggest Big Data trade show Quarry Summit Fair, we created the Plumline Census. This first national research on Big Data aims at providing insight in use of Big Data. The survey is built on five corner stones: Organization, Data, Technology, Skills and Process.

Design
We are looking for an insightful representation of the key-results of the survey, based on the five corner stones. It may also very well be multiple infographics in order to decrease the information density, but I'll leave that to you.

We are looking for a fresh, funky and attractive design, that is easily understood. Please use the colors (orange and blue) of the survey report. For more information see: http://www.nexoraflux.example/static/images/plumlinecensus/plumlinecensus-resultaten-web.pdf

```html
<!DOCTYPE html>
<html lang="en">
<head>
<meta charset="utf-8">
<title>Infographic of Plumline Census</title>
<link rel="stylesheet" href="https://fonts.googleapis.com/css2?family=Oswald:wght@400;500&family=Open+Sans:wght@400;600;700&display=swap">
<style>
:root{
  --blue:#2e75b8;
  --orange:#f7941d;
  --orange-deep:#f26d3d;
  --gold:#fbb040;
  --ink:#333333;
  --badge:#58595b;
  --cell:#d1d3d4;
  --paper:#f2f2f2;
  --white:#ffffff;
}
*{margin:0;padding:0;box-sizing:border-box}
html,body{width:1200px;height:2616px;overflow:hidden;background:var(--blue)}
body{font-family:"Open Sans",Arial,sans-serif;color:var(--white)}
.artboard{position:absolute;left:0;top:0;width:688px;height:1500px;transform:scale(1.744186);transform-origin:0 0;background:var(--blue);overflow:hidden}
.abs{position:absolute}

/* header */
.ribbon-tab{position:absolute;top:0;width:40px;height:34px;background:var(--orange-deep)}
.ribbon-tab.left{left:80px;clip-path:polygon(100% 0,100% 100%,0 0)}
.ribbon-tab.right{left:568px;width:120px;height:100px;clip-path:polygon(0 0,100% 0,100% 100%,20% 34%,0 34%)}
.masthead{position:absolute;left:107px;top:0;width:480px;height:133px;background:var(--orange);border-radius:0 0 16px 16px;text-align:center}
.masthead h1{font-family:"Oswald",Impact,sans-serif;font-weight:500;font-size:37px;letter-spacing:.2px;margin-top:40px;line-height:1;text-transform:uppercase}
.masthead .source{font-size:10px;margin-top:14px;opacity:.92}

/* section bars */
.section-tag{position:absolute;left:198px;width:290px;height:47px;font-family:"Oswald",Impact,sans-serif;font-weight:500;font-size:31px;line-height:47px;text-align:center;color:var(--white);text-transform:uppercase}
.section-tag.orange{background:var(--orange)}
.section-tag.blue{background:var(--blue)}
.panel-data{position:absolute;left:0;top:710px;width:688px;height:578px;background:var(--paper)}

/* dividers */
.dash-v{position:absolute;width:0;border-left:1.5px dashed rgba(255,255,255,.55)}
.dash-h{position:absolute;height:0;border-top:1.5px dashed rgba(255,255,255,.55)}
.on-paper.dash-v{border-left-color:#9a9a9a}
.on-paper.dash-h{border-top-color:#9a9a9a}

/* number badges */
.badge{position:absolute;width:48px;height:48px;border-radius:50%;background:var(--badge);border:4px solid var(--white);box-shadow:0 0 0 2px #c9c9c9;font-weight:700;font-size:16px;line-height:40px;text-align:center;color:var(--white)}
.item-title{position:absolute;font-weight:700;font-size:19px;line-height:23px}
.on-paper{color:var(--ink)}
.body-copy{position:absolute;font-size:12px;line-height:15px}

/* donut */
.donut{position:absolute;width:90px;height:90px}
.donut-label{position:absolute;font-weight:700;font-size:17px;color:var(--gold);width:90px;text-align:center;line-height:90px}

/* cell bars */
.stat{position:absolute}
.stat-label{font-size:9px;line-height:11px}
.stat-label b{font-weight:700}
.cells{display:flex;gap:1.5px;margin-top:2px}
.cell{display:block;width:9.5px;height:8px;background:var(--cell)}
.cell.full{background:var(--orange)}
.cell.part{background:linear-gradient(90deg,var(--orange) var(--fill),var(--cell) var(--fill))}
.stat.large .cells{gap:3px;margin-top:6px}
.stat.large .cell{width:16.7px;height:16px}
.stat.medium .cells{gap:3px;margin-top:6px}
.stat.medium .cell{width:15px;height:15px}
.stat-row{display:flex;font-size:12px;line-height:14px}
.stat-row b{font-weight:700;font-size:13px;width:34px}

/* pins */
.pin{position:absolute;width:48px;text-align:center}
.pin svg{display:block;margin:0 auto}
.pin-value{position:absolute;left:0;top:0;width:48px;line-height:40px;font-weight:700;font-size:12px;color:var(--blue)}
.pin.small .pin-value{font-size:12px;line-height:38px}
.pin-caption{position:absolute;font-size:10px;font-weight:600;line-height:12px;text-align:center;white-space:nowrap}
.pin-caption.on-paper{font-weight:400;font-size:11px}
</style>
</head>
<body>
<main class="artboard">

  <!-- header -->
  <div class="ribbon-tab left"></div>
  <div class="ribbon-tab right"></div>
  <header class="masthead">
    <h1>Infographic of Plumline Census</h1>
    <p class="source">Source: Plumline Census 2015, 186 participants</p>
  </header>

  <!-- ORGANIZATION -->
  <div class="section-tag orange" style="top:166px">Organization</div>
  <div class="dash-v" style="left:344px;top:230px;height:465px"></div>
  <div class="dash-h" style="left:25px;top:443px;width:640px"></div>

  <div class="badge" style="left:28px;top:244px">01</div>
  <h2 class="item-title" style="left:118px;top:253px">Opportunities Of<br>Data</h2>
  <svg class="donut" style="left:70px;top:317px" viewBox="0 0 90 90" aria-hidden="true">
    <circle cx="45" cy="45" r="35" fill="none" stroke="#d1d3d4" stroke-width="12"/>
    <circle cx="45" cy="45" r="35" fill="none" stroke="#f7941d" stroke-width="12" stroke-dasharray="202.3 219.9" transform="rotate(-70 45 45)"/>
  </svg>
  <div class="donut-label" style="left:70px;top:317px">92%</div>
  <p class="body-copy" style="left:170px;top:340px;width:155px">92% of organizations say that the opportunities of data for their organization are big.</p>

  <div class="badge" style="left:369px;top:246px">02</div>
  <h2 class="item-title" style="left:477px;top:262px">Budget</h2>
  <svg class="donut" style="left:413px;top:310px" viewBox="0 0 90 90" aria-hidden="true">
    <circle cx="45" cy="45" r="35" fill="none" stroke="#d1d3d4" stroke-width="12"/>
    <circle cx="45" cy="45" r="35" fill="none" stroke="#f7941d" stroke-width="12" stroke-dasharray="151.7 219.9" transform="rotate(-90 45 45)"/>
  </svg>
  <div class="donut-label" style="left:413px;top:310px">69%</div>
  <p class="body-copy" style="left:517px;top:334px;width:150px">69% of organizations will increase their budget for big data in 2016</p>

  <div class="badge" style="left:26px;top:491px">03</div>
  <h2 class="item-title" style="left:93px;top:490px">Is Big Data part of your<br>organization strategy?</h2>
  <div class="stat" style="left:52px;top:581px">
    <p class="stat-label"><b>37%</b> agree</p>
    <div class="cells"><i class="cell full"></i><i class="cell full"></i><i class="cell full"></i><i class="cell part" style="--fill:70%"></i><i class="cell"></i><i class="cell"></i><i class="cell"></i><i class="cell"></i><i class="cell"></i><i class="cell"></i></div>
  </div>
  <div class="stat" style="left:231px;top:584px">
    <p class="stat-label"><b>27%</b> partially agree</p>
    <div class="cells"><i class="cell full"></i><i class="cell full"></i><i class="cell part" style="--fill:70%"></i><i class="cell"></i><i class="cell"></i><i class="cell"></i><i class="cell"></i><i class="cell"></i><i class="cell"></i><i class="cell"></i></div>
  </div>
  <div class="stat" style="left:52px;top:616px">
    <p class="stat-label"><b>11%</b> partially disagrees</p>
    <div class="cells"><i class="cell full"></i><i class="cell part" style="--fill:10%"></i><i class="cell"></i><i class="cell"></i><i class="cell"></i><i class="cell"></i><i class="cell"></i><i class="cell"></i><i class="cell"></i><i class="cell"></i></div>
  </div>
  <div class="stat" style="left:231px;top:619px">
    <p class="stat-label"><b>12%</b> totally disagrees</p>
    <div class="cells"><i class="cell full"></i><i class="cell part" style="--fill:20%"></i><i class="cell"></i><i class="cell"></i><i class="cell"></i><i class="cell"></i><i class="cell"></i><i class="cell"></i><i class="cell"></i><i class="cell"></i></div>
  </div>

  <div class="badge" style="left:359px;top:491px">04</div>
  <h2 class="item-title" style="left:434px;top:496px">Success Factors</h2>
  <p class="body-copy" style="left:368px;top:567px;width:112px;font-size:10px;line-height:12px">The most important factors of a successful implementation of a big data strategy are:</p>
  <div class="pin" style="left:496px;top:539px">
    <svg width="48" height="54" viewBox="0 0 48 54" aria-hidden="true"><path d="M24 52 L16 40 A21 21 0 1 1 32 40 Z" fill="#f7941d"/><circle cx="24" cy="22" r="17" fill="#fff"/></svg>
    <span class="pin-value" style="line-height:46px;font-size:14px">28%</span>
  </div>
  <p class="pin-caption" style="left:480px;top:603px;width:80px">Company Vision</p>
  <div class="pin" style="left:592px;top:539px">
    <svg width="48" height="54" viewBox="0 0 48 54" aria-hidden="true"><path d="M24 52 L16 40 A21 21 0 1 1 32 40 Z" fill="#f7941d"/><circle cx="24" cy="22" r="17" fill="#fff"/></svg>
    <span class="pin-value" style="line-height:46px;font-size:14px">19%</span>
  </div>
  <p class="pin-caption" style="left:572px;top:603px;width:88px">Support from the<br>management</p>
  <p class="abs" style="left:400px;top:647px;width:225px;text-align:center;font-size:10px">These factors are more important than:</p>
  <p class="abs" style="left:400px;top:659px;width:225px;text-align:center;font-size:14px;font-weight:700;color:var(--gold)">Budget, Training, Talent</p>

  <!-- DATA -->
  <section class="panel-data"></section>
  <div class="section-tag blue" style="top:730px">Data</div>
  <div class="dash-v on-paper" style="left:343px;top:795px;height:300px"></div>
  <div class="dash-h on-paper" style="left:35px;top:1103px;width:615px"></div>

  <div class="badge" style="left:36px;top:805px">01</div>
  <h2 class="item-title on-paper" style="left:98px;top:801px">What Are The Biggest<br>Challenges In The Field<br>Of Data?</h2>
  <p class="body-copy on-paper" style="left:55px;top:881px;width:270px">Only 8% of organizations find optimizing a predictive model the most difficult challenge in the field of data. Top 3 challenges are:</p>
  <div class="stat large on-paper" style="left:67px;top:945px">
    <p class="stat-row"><b>18%</b> Time to experiment</p>
    <div class="cells"><i class="cell full"></i><i class="cell part" style="--fill:80%"></i><i class="cell"></i><i class="cell"></i><i class="cell"></i><i class="cell"></i><i class="cell"></i><i class="cell"></i><i class="cell"></i><i class="cell"></i></div>
  </div>
  <div class="stat large on-paper" style="left:67px;top:994px">
    <p class="stat-row"><b>15%</b> Making data available</p>
    <div class="cells"><i class="cell full"></i><i class="cell part" style="--fill:50%"></i><i class="cell"></i><i class="cell"></i><i class="cell"></i><i class="cell"></i><i class="cell"></i><i class="cell"></i><i class="cell"></i><i class="cell"></i></div>
  </div>
  <div class="stat large on-paper" style="left:67px;top:1041px">
    <p class="stat-row"><b>14%</b> Investing in data scientists</p>
    <div class="cells"><i class="cell full"></i><i class="cell part" style="--fill:40%"></i><i class="cell"></i><i class="cell"></i><i class="cell"></i><i class="cell"></i><i class="cell"></i><i class="cell"></i><i class="cell"></i><i class="cell"></i></div>
  </div>

  <div class="badge" style="left:361px;top:812px">02</div>
  <h2 class="item-title on-paper" style="left:423px;top:801px">Most Used Data Sources</h2>
  <p class="abs on-paper" style="left:405px;top:856px;width:240px;text-align:center;font-size:12px">THE MOST USED DATA SOURCES ARE</p>
  <div class="pin small" style="left:438px;top:881px">
    <svg width="48" height="50" viewBox="0 0 48 50" aria-hidden="true"><path d="M24 49 L17 38 A20 20 0 1 1 31 38 Z" fill="#f7941d"/><circle cx="24" cy="21" r="16" fill="#fff"/></svg>
    <span class="pin-value" style="line-height:43px;font-size:11px">18%</span>
  </div>
  <p class="pin-caption on-paper" style="left:402px;top:937px;width:120px">CRM / Customer data</p>
  <div class="pin small" style="left:560px;top:881px">
    <svg width="48" height="50" viewBox="0 0 48 50" aria-hidden="true"><path d="M24 49 L17 38 A20 20 0 1 1 31 38 Z" fill="#f7941d"/><circle cx="24" cy="21" r="16" fill="#fff"/></svg>
    <span class="pin-value" style="line-height:43px;font-size:11px">18%</span>
  </div>
  <p class="pin-caption on-paper" style="left:534px;top:937px;width:100px">Website statistics</p>
  <p class="abs on-paper" style="left:405px;top:968px;width:240px;text-align:center;font-size:21px">LEAST USED ARE</p>
  <div class="pin small" style="left:443px;top:1005px">
    <svg width="48" height="50" viewBox="0 0 48 50" aria-hidden="true"><path d="M24 49 L17 38 A20 20 0 1 1 31 38 Z" fill="#f7941d"/><circle cx="24" cy="21" r="16" fill="#fff"/></svg>
    <span class="pin-value" style="line-height:43px;font-size:12px">2%</span>
  </div>
  <p class="pin-caption on-paper" style="left:447px;top:1061px;width:40px">Audio</p>
  <div class="pin small" style="left:496px;top:1005px">
    <svg width="48" height="50" viewBox="0 0 48 50" aria-hidden="true"><path d="M24 49 L17 38 A20 20 0 1 1 31 38 Z" fill="#f7941d"/><circle cx="24" cy="21" r="16" fill="#fff"/></svg>
    <span class="pin-value" style="line-height:43px;font-size:12px">5%</span>
  </div>
  <p class="pin-caption on-paper" style="left:500px;top:1061px;width:40px">Video</p>
  <div class="pin small" style="left:550px;top:1005px">
    <svg width="48" height="50" viewBox="0 0 48 50" aria-hidden="true"><path d="M24 49 L17 38 A20 20 0 1 1 31 38 Z" fill="#f7941d"/><circle cx="24" cy="21" r="16" fill="#fff"/></svg>
    <span class="pin-value" style="line-height:43px;font-size:12px">6%</span>
  </div>
  <p class="pin-caption on-paper" style="left:554px;top:1061px;width:40px">Image</p>

  <div class="badge" style="left:101px;top:1113px">03</div>
  <h2 class="item-title on-paper" style="left:62px;top:1176px">Data Security</h2>
  <p class="body-copy on-paper" style="left:62px;top:1205px;width:180px;font-size:14px;line-height:17px">Are data stored securely within your organization?</p>
  <div class="stat medium on-paper" style="left:248px;top:1153px">
    <p class="stat-row"><b style="width:53px">25%</b> Agrees</p>
    <div class="cells"><i class="cell full"></i><i class="cell full"></i><i class="cell part" style="--fill:50%"></i><i class="cell"></i><i class="cell"></i><i class="cell"></i><i class="cell"></i><i class="cell"></i><i class="cell"></i><i class="cell"></i></div>
  </div>
  <div class="stat medium on-paper" style="left:457px;top:1153px">
    <p class="stat-row"><b style="width:65px">32%</b> Partially Agrees</p>
    <div class="cells"><i class="cell full"></i><i class="cell full"></i><i class="cell full"></i><i class="cell part" style="--fill:20%"></i><i class="cell"></i><i class="cell"></i><i class="cell"></i><i class="cell"></i><i class="cell"></i><i class="cell"></i></div>
  </div>
  <div class="stat medium on-paper" style="left:248px;top:1203px">
    <p class="stat-row"><b style="width:53px">12%</b> Partially Disagrees</p>
    <div class="cells"><i class="cell full"></i><i class="cell part" style="--fill:20%"></i><i class="cell"></i><i class="cell"></i><i class="cell"></i><i class="cell"></i><i class="cell"></i><i class="cell"></i><i class="cell"></i><i class="cell"></i></div>
  </div>
  <div class="stat medium on-paper" style="left:457px;top:1203px">
    <p class="stat-row"><b style="width:67px">7%</b> Totally Agrees</p>
    <div class="cells"><i class="cell part" style="--fill:70%"></i><i class="cell"></i><i class="cell"></i><i class="cell"></i><i class="cell"></i><i class="cell"></i><i class="cell"></i><i class="cell"></i><i class="cell"></i><i class="cell"></i></div>
  </div>

  <!-- TECHNOLOGY -->
  <div class="section-tag orange" style="top:1300px">Technology</div>
  <div class="dash-v" style="left:330px;top:1370px;height:130px"></div>
  <div class="badge" style="left:38px;top:1381px">01</div>
  <h2 class="item-title" style="left:140px;top:1433px">Type Of Software<br>Used</h2>
  <div class="badge" style="left:384px;top:1381px">02</div>
  <h2 class="item-title" style="left:458px;top:1393px">Most Popular<br>Technologies</h2>

</main>
</body>
</html>
```